ORVAN LOGIC LTD

See website just wanted it updated and more fresh ; https://www.orvan-logic.co.uk

Coding

Coded - Design and coding required

Colors

Designer to choose colors to be used in the design.

```html
<!DOCTYPE html>
<html lang="en">
<head>
<meta charset="utf-8">
<title>Orvan Logic – Education Support and Installation</title>
<link rel="stylesheet" href="https://fonts.googleapis.com/css2?family=Josefin+Sans:wght@600;700&family=Lato:wght@400;700&display=swap">
<style>
:root{
  --orange:#f07535;
  --orange-deep:#e8561c;
  --peach:#ffc995;
  --blue:#0a6bbf;
  --blue-light:#2f8fe0;
  --ink:#1d1d1d;
  --text:#666;
  --grey-bg:#f3f3f3;
  --white:#fff;
  --footer:#24201f;
}
*{margin:0;padding:0;box-sizing:border-box}
html,body{width:1200px;height:4043px;overflow:hidden}
body{position:relative;background:var(--white);font-family:"Lato",sans-serif;color:var(--text)}
.abs{position:absolute}
.heading{font-family:"Josefin Sans",sans-serif;font-weight:700;font-variant:small-caps;color:var(--ink);letter-spacing:.5px;line-height:1.2}
.center{text-align:center}
.btn{position:absolute;display:flex;align-items:center;justify-content:center;border-radius:30px;color:var(--white);font-family:"Josefin Sans",sans-serif;font-weight:700;font-variant:small-caps;font-size:17px;letter-spacing:.4px}
.btn-blue{background:var(--blue)}
.btn-orange{background:var(--orange-deep)}
.para{font-size:11px;line-height:19.5px}

/* hero */
.hero-art{left:0;top:0}
.brand{left:162px;top:30px;color:var(--white);font-family:"Lato",sans-serif;font-weight:700;font-size:26px;letter-spacing:.5px}
.nav{left:450px;top:40px;display:flex;gap:27px;font-size:11px;font-weight:700;color:var(--white)}
.user{left:814px;top:28px;width:38px;height:38px;border:2px solid var(--white);border-radius:50%}
.hero-title{left:162px;top:218px;width:640px;font-size:40px;color:var(--white)}
.hero-text{left:163px;top:322px;width:540px;font-size:12.5px;line-height:20px;color:var(--white)}
.hero-btn{left:162px;top:400px;width:187px;height:50px}
.slide-arrows{left:563px;top:576px;display:flex;gap:18px}

/* about */
.about-title{left:0;top:724px;width:1200px;font-size:31px}
.about-text{left:386px;top:774px;width:428px}
.video{left:326px;top:955px;width:548px;height:275px;border-radius:47px 47px 0 0;background:linear-gradient(135deg,#6b1d22,#3a1416 55%,#7a3526)}
.play{left:580px;top:1080px}

.cta{left:195px;width:810px;height:298px;border-radius:26px;background:radial-gradient(circle at 50% 60%,#fba06b 0,#f58449 45%,var(--orange) 100%)}
.cta-1{top:1230px}
.cta-title{left:195px;width:810px;font-size:30px;color:var(--white)}
.cta-text{left:380px;width:440px;font-size:11px;line-height:19px;color:#ffe3d1}
.call-btn{left:529px;top:1417px;width:143px;height:44px;font-size:15px}

.chip-photo{left:262px;top:1528px;width:300px;height:443px;border-radius:0 0 150px 150px;background:linear-gradient(160deg,#2a3035,#48525a 45%,#7d5c66)}
.support-title{left:612px;top:1565px;width:420px;font-size:30px}
.support-text{left:612px;top:1655px;width:382px}
.more-btn{left:612px;top:1833px;width:163px;height:44px;font-size:15px}

/* services */
.grey-wave{left:0;top:1990px}
.grey-band{left:0;top:2060px;width:1200px;height:1674px;background:var(--grey-bg)}
.services-title{left:0;top:2122px;width:1200px;font-size:30px}
.services-text{left:390px;top:2173px;width:420px}
.card{top:2253px;width:276px;height:322px;background:var(--white);border-radius:8px;text-align:center}
.card-icon{position:absolute;left:93px;top:29px;width:90px;height:90px;border-radius:50%;background:linear-gradient(135deg,var(--blue-light),var(--blue));display:flex;align-items:center;justify-content:center}
.card-title{position:absolute;left:0;top:145px;width:100%;font-size:14.5px}
.card-text{position:absolute;left:22px;top:176px;width:232px;font-size:11px;line-height:19px}
.card-link{position:absolute;left:0;top:272px;width:100%;font-family:"Josefin Sans",sans-serif;font-weight:700;font-variant:small-caps;font-size:12.5px;color:var(--orange-deep)}

.cta-2{top:2652px}
.quote{left:335px;top:2748px;width:530px;font-size:12.5px;line-height:22.5px;color:var(--white)}
.quote-name{left:420px;top:2874px;width:360px;font-size:11px;line-height:19px;font-weight:700;color:#111}
.q-arrow{width:26px;height:26px;border:1.5px solid var(--white);border-radius:4px;top:2788px}

.kids-photo{left:648px;top:2950px;width:300px;height:443px;border-radius:0 0 150px 150px;background:linear-gradient(160deg,#3b4a52,#4f5d63 50%,#c46a53)}
.why-title{left:162px;top:3010px;font-size:30px}
.why-list{left:162px;top:3068px;list-style:none;font-size:11px;line-height:19.5px}
.why-list li{display:flex;align-items:center;gap:8px}
.know-btn{left:162px;top:3262px;width:141px;height:44px;font-size:15px}

.stay-title{left:0;top:3447px;width:1200px;font-size:30px}
.stay-text{left:390px;top:3511px;width:420px}
.email{left:425px;top:3571px;width:350px;height:41px;border-radius:21px;background:var(--white);font-size:11px;color:#777;padding:14px 0 0 22px}
.sub-btn{left:521px;top:3634px;width:150px;height:38px;font-size:15px}

/* footer */
.footer{left:0;top:3734px;width:1200px;height:309px;background:radial-gradient(ellipse at 75% 45%,#4a3a33 0,var(--footer) 60%)}
.foot-brand{left:0;top:3792px;width:1200px;text-align:center;color:var(--white);font-weight:700;font-size:28px;letter-spacing:.5px}
.social{top:3880px;width:36px;height:36px;border:1.5px solid var(--orange);border-radius:50%}
.foot-nav{left:0;top:3944px;width:1200px;display:flex;justify-content:center;gap:30px;font-size:11px;color:#ddd}
.foot-rule{left:162px;top:3988px;width:876px;height:1px;background:#4b4644}
.copy{left:0;top:4008px;width:1200px;text-align:center;font-size:10px;color:#ccc}
</style>
</head>
<body>

<!-- Hero -->
<svg class="abs hero-art" width="1200" height="720" viewBox="0 0 1200 720" aria-hidden="true">
  <defs>
    <linearGradient id="heroGrad" x1="0" y1="0.6" x2="1" y2="0">
      <stop offset="0" stop-color="#f07535"/>
      <stop offset="0.55" stop-color="#ffa86a"/>
      <stop offset="1" stop-color="#ffc995"/>
    </linearGradient>
    <linearGradient id="photoGrad" x1="0" y1="0" x2="1" y2="1">
      <stop offset="0" stop-color="#5a4634"/>
      <stop offset="0.5" stop-color="#a37650"/>
      <stop offset="1" stop-color="#6e5a4c"/>
    </linearGradient>
  </defs>
  <path d="M0 0 H1008 C860 170 700 400 470 560 C320 660 150 700 0 712 Z" fill="url(#heroGrad)"/>
  <path role="img" aria-label="Photo of a teacher helping two pupils with a tablet" d="M1008 0 H1200 V545 C1140 640 1050 688 955 682 C770 672 640 545 648 385 C655 250 730 175 820 125 C890 85 960 50 1008 0 Z" fill="url(#photoGrad)"/>
</svg>
<div class="abs brand">Orvan Logic</div>
<nav class="abs nav"><span>Home</span><span>About Us</span><span>Services</span><span>Help Desk</span><span>Contact Us</span></nav>
<div class="abs user" aria-label="Account">
  <svg width="34" height="34" viewBox="0 0 34 34" aria-hidden="true"><circle cx="17" cy="13" r="4.5" fill="#fff"/><path d="M9.5 25c0-5 3.5-7 7.5-7s7.5 2 7.5 7z" fill="#fff"/></svg>
</div>
<h1 class="abs heading hero-title">Education, Support and<br>Installation of All Technologies</h1>
<p class="abs hero-text">Lorem Ipsum is simply dummy text of the printing and typesetting industry. Lorem Ipsum has been the industry's standard dummy text ever since the 1500s</p>
<a class="btn btn-blue hero-btn">Get In Touch</a>
<div class="abs slide-arrows">
  <svg width="28" height="28" viewBox="0 0 28 28" aria-label="Previous"><circle cx="14" cy="14" r="12" fill="none" stroke="#0a6bbf" stroke-width="2.5"/><path d="M19 14H9M13 9.5 8.5 14 13 18.5" fill="none" stroke="#0a6bbf" stroke-width="2.5" stroke-linecap="round" stroke-linejoin="round"/></svg>
  <svg width="28" height="28" viewBox="0 0 28 28" aria-label="Next"><circle cx="14" cy="14" r="12" fill="none" stroke="#0a6bbf" stroke-width="2.5"/><path d="M9 14h10M15 9.5l4.5 4.5-4.5 4.5" fill="none" stroke="#0a6bbf" stroke-width="2.5" stroke-linecap="round" stroke-linejoin="round"/></svg>
</div>

<!-- About -->
<h2 class="abs heading center about-title">About Orvan Logic</h2>
<p class="abs para center about-text">Lorem Ipsum is simply dummy text of the printing and typesetting industry. Lorem Ipsum has been the industry's standard dummy text ever since the 1500s, when an unknown printer took a galley of type and scrambled it to make a type specimen book. It has survived not only five centuries, but also the leap into electronic typesetting, remaining essentially unchanged. It was popularised in the 1960s with the release of Letterline sheets containing Lorem Ipsum passages, and more recently with desktop publishing software like Pagewright including versions of Lorem Ipsum.</p>
<div class="abs video" role="img" aria-label="Video still of a young boy in glasses in front of bookshelves"></div>
<svg class="abs play" width="40" height="40" viewBox="0 0 40 40" aria-label="Play video"><circle cx="20" cy="20" r="17" fill="none" stroke="#fff" stroke-width="2.5"/><path d="M16 12.5v15l11.5-7.5z" fill="#fff"/></svg>

<div class="abs cta cta-1"></div>
<h2 class="abs heading center cta-title" style="top:1284px">We'd love to Hear From you</h2>
<p class="abs center cta-text" style="top:1336px">Whether you have a question about features, services, plans, need demo or anything else, our team is ready to answer all your questions, don't hasitate call us now</p>
<a class="btn btn-orange call-btn">Call Us Now</a>

<div class="abs chip-photo" role="img" aria-label="Close-up photo of a computer circuit board"></div>
<h2 class="abs heading support-title">Complete Primary and Secondary School Support</h2>
<p class="abs para support-text">We offer support in all aspects of ICT in education, from technical faults to assisting teachers and coordinators to meet the requirements of the computing curriculum. We offer support in all aspects of ICT in education, from technical faults to assisting teachers and coordinators to meet the requirements of the computing curriculum. We offer support in all aspects of ICT in education, from technical faults to assisting teachers and coordinators to meet the requirements of the computing curriculum.</p>
<a class="btn btn-blue more-btn">Find Out More</a>

<!-- Services -->
<svg class="abs grey-wave" width="1200" height="80" viewBox="0 0 1200 80" aria-hidden="true"><path d="M0 30 C150 5 280 0 420 25 C560 50 700 55 860 30 C1000 10 1100 5 1200 15 V80 H0 Z" fill="#f3f3f3"/></svg>
<div class="abs grey-band"></div>
<h2 class="abs heading center services-title">Orvan Logic Services</h2>
<p class="abs para center services-text">Lorem Ipsum is simply dummy text of the printing and typesetting industry. Lorem Ipsum has been the industry's standard dummy text ever since the 1500s.</p>

<div class="abs card" style="left:162px">
  <div class="card-icon"><svg width="50" height="50" viewBox="0 0 50 50" fill="none" stroke="#fff" stroke-width="2.5" stroke-linecap="round" stroke-linejoin="round" aria-hidden="true"><path d="M10 40 30 20M33 8a8 8 0 0 0-4 11l2 2a8 8 0 0 0 11-4l-5 1-3-3z"/><path d="M40 40 20 20M12 8l-4 4 5 5 4-4zM17 13l4 4"/></svg></div>
  <h3 class="heading card-title">ICT Support</h3>
  <p class="card-text">We provide a wide range of ICT support packages, which all include regular onsite visits, telephone, email and helpdesk support plus secure remote assistance</p>
  <span class="card-link">Read More &nbsp;»</span>
</div>
<div class="abs card" style="left:461px">
  <div class="card-icon"><svg width="50" height="50" viewBox="0 0 50 50" fill="none" stroke="#fff" stroke-width="2.5" stroke-linejoin="round" aria-hidden="true"><rect x="11" y="9" width="28" height="22" rx="2"/><path d="M16 15h18M16 20h18M16 25h12M22 31v5h6v-5M13 40h24"/></svg></div>
  <h3 class="heading card-title">Hardware Sales</h3>
  <p class="card-text">We supply and install hardware from the world's leading manufacturers including: Kor, Tovana, Acro, Smeed, Benvo and many moreWe supply and install hardware from the.</p>
  <span class="card-link">Read More &nbsp;»</span>
</div>
<div class="abs card" style="left:761px">
  <div class="card-icon"><svg width="50" height="50" viewBox="0 0 50 50" fill="none" stroke="#fff" stroke-width="2.5" stroke-linecap="round" aria-hidden="true"><path d="M15 26a7 7 0 0 1 1-14 10 10 0 0 1 19 2 6 6 0 0 1 0 12z"/><path d="M25 26v10M17 26v6l-4 4M33 26v6l4 4"/><circle cx="25" cy="39" r="2.5"/><circle cx="12" cy="39" r="2.5"/><circle cx="38" cy="39" r="2.5"/></svg></div>
  <h3 class="heading card-title">Cloud &amp; Hosting Services</h3>
  <p class="card-text">We offer an extensive range of cloud and hosting services including websites, domains, blogs, emails and cloud storage solutions.services including websites</p>
  <span class="card-link">Read More &nbsp;»</span>
</div>

<!-- Testimonial -->
<div class="abs cta cta-2"></div>
<h2 class="abs heading center cta-title" style="top:2692px">In their own words</h2>
<p class="abs center quote">"The team at Orvan Logic offer a fantastic service. They are reliable and approachable and ensure the smooth running of our school network. Their technical knowledge is excellent and love the challenge of solving new problems! Nothing is too much for Rory as he understands how schools operate. His service includes cover ahead of school inspections. and is keen to stay up to date with the latest developments. "</p>
<p class="abs center quote-name">Maren Holloway-Pike, Headteacher at Fenwick Lane Junior School</p>
<svg class="abs q-arrow" style="left:241px" viewBox="0 0 26 26" aria-label="Previous quote"><path d="M15 7 9 13l6 6" fill="none" stroke="#fff" stroke-width="1.8"/></svg>
<svg class="abs q-arrow" style="left:932px" viewBox="0 0 26 26" aria-label="Next quote"><path d="M11 7l6 6-6 6" fill="none" stroke="#fff" stroke-width="1.8"/></svg>

<!-- Why -->
<div class="abs kids-photo" role="img" aria-label="Photo of two happy schoolgirls raising their hands"></div>
<h2 class="abs heading why-title">Why Orvan Logic</h2>
<ul class="abs why-list">
  <li><svg width="14" height="10" viewBox="0 0 14 10" aria-hidden="true"><path d="M1 5l3 3 6-7M6 8l7-7" fill="none" stroke="#e8561c" stroke-width="1.5"/></svg>Unlimited Call outs between 7.00am – 6.00pm</li>
  <li><svg width="14" height="10" viewBox="0 0 14 10" aria-hidden="true"><path d="M1 5l3 3 6-7M6 8l7-7" fill="none" stroke="#e8561c" stroke-width="1.5"/></svg>Extra support visits during school inspections</li>
  <li><svg width="14" height="10" viewBox="0 0 14 10" aria-hidden="true"><path d="M1 5l3 3 6-7M6 8l7-7" fill="none" stroke="#e8561c" stroke-width="1.5"/></svg>Remote access support for servers, computers and laptops</li>
  <li><svg width="14" height="10" viewBox="0 0 14 10" aria-hidden="true"><path d="M1 5l3 3 6-7M6 8l7-7" fill="none" stroke="#e8561c" stroke-width="1.5"/></svg>Email and Telephone Support</li>
  <li><svg width="14" height="10" viewBox="0 0 14 10" aria-hidden="true"><path d="M1 5l3 3 6-7M6 8l7-7" fill="none" stroke="#e8561c" stroke-width="1.5"/></svg>Ticket help desk, with guaranteed same day reply</li>
  <li><svg width="14" height="10" viewBox="0 0 14 10" aria-hidden="true"><path d="M1 5l3 3 6-7M6 8l7-7" fill="none" stroke="#e8561c" stroke-width="1.5"/></svg>Cloud storage for all staff members</li>
  <li><svg width="14" height="10" viewBox="0 0 14 10" aria-hidden="true"><path d="M1 5l3 3 6-7M6 8l7-7" fill="none" stroke="#e8561c" stroke-width="1.5"/></svg>Regular management meetings</li>
  <li><svg width="14" height="10" viewBox="0 0 14 10" aria-hidden="true"><path d="M1 5l3 3 6-7M6 8l7-7" fill="none" stroke="#e8561c" stroke-width="1.5"/></svg>Support levels to suit your individual needs.</li>
</ul>
<a class="btn btn-blue know-btn">Know More</a>

<!-- Newsletter -->
<h2 class="abs heading center stay-title">Stay Connect with Us</h2>
<p class="abs para center stay-text">Lorem Ipsum is simply dummy text of the printing and typesetting industry. Lorem Ipsum has been the industry's standard dummy text ever since the 1500s.</p>
<div class="abs email">Enter Email:</div>
<a class="btn btn-orange sub-btn">Subscribe Now!</a>

<!-- Footer -->
<footer class="abs footer" role="img" aria-label="Dark background photo of a pupil at school"></footer>
<div class="abs foot-brand">Orvan Logic</div>
<span class="abs social" style="left:536px" aria-label="Social profile"></span>
<span class="abs social" style="left:581px" aria-label="Social profile"></span>
<span class="abs social" style="left:627px" aria-label="Social profile"></span>
<nav class="abs foot-nav"><span>Home</span><span>About Us</span><span>Services</span><span>Help Desk</span><span>Contact Us</span></nav>
<div class="abs foot-rule"></div>
<p class="abs copy">Copyright © 2020 Orvan Logic Ltd. All Rights Reserved. Terms &amp; Conditions.</p>

</body>
</html>
```